Broschüre für Bauingenieurbüro
Zielgruppe
Wir sind ein kleines Bauingenieurbüro mit bis 10 Mitarbeiterinnen. Wir wollen uns bei bestehenden Kunden mit der Broschüre in Erinnerung rufen und für neue Kunden genügend Informationen und Schlagkraft aufzeigen, dass diese uns Aufträge zukommen lassen. Zu unseren Kunden gehören hauptsächlich Architekturbüros und wenige Privatpersonen als Bauherren.
Aufgabenstellung
Wir möchten die Broschüre auf A3 doppelseitig mit einem Falz in der Mitte haben (Zusammengefaltet soll die Broschüre das Format A4 aufweisen). Unser bestehendes Porträt wird dem Auftrag beigelegt (PDF Rohversion Seite 3 und 4). Das Dokument 'Veränderung Firmenporträt 220818' zeigt unsere Wünsche auf. Das Design der Broschüre soll dann in einem weiteren Schritt auch auf die Homepage übergehen.

```html
<!DOCTYPE html>
<html lang="de">
<head>
<meta charset="utf-8">
<title>Kurzportrait Broschüre – kernbau ingenieure</title>
<link rel="stylesheet" href="https://fonts.googleapis.com/css2?family=Barlow:wght@400;600&family=Lexend+Exa:wght@300;400&display=swap">
<style>
:root{
  --stage-dark:#2c2c2c;
  --stage-light:#e4e4e4;
  --paper:#ffffff;
  --paper-shade:#f2f2f2;
  --paper-warm:#f4f0e9;
  --ink:#3c3c3c;
  --ink-soft:#6a6a6a;
  --tan:#c6b595;
  --tan-head:#c9b48f;
  --chip-grey:#ececec;
  --cover-dark:#3a3937;
  --guide:#9fc6ec;
  --label:#8a8a8a;
}
*{margin:0;padding:0;box-sizing:border-box}
html,body{width:1200px;height:2832px;overflow:hidden}
body{position:relative;background:var(--stage-light);font-family:"Barlow",sans-serif;color:var(--ink)}
.stage-dark{position:absolute;left:0;top:0;width:1200px;height:1198px;background:var(--stage-dark)}
.stage-label{position:absolute;font-family:"Lexend Exa",sans-serif;font-weight:300;font-size:12.5px;color:var(--label);letter-spacing:.5px;transform:translateX(-50%)}
.spread{position:absolute;width:960px;height:679px;box-shadow:0 2px 10px rgba(0,0,0,.12)}
.single{position:absolute;width:480px;height:679px}
.mini{transform:scale(.625);transform-origin:0 0}
.page{position:absolute;top:0;width:480px;height:679px;background:var(--paper);overflow:hidden}
.page .bg{position:absolute;left:0;top:0;width:480px;height:679px}
.abs{position:absolute}
.h-page{position:absolute;font-family:"Lexend Exa",sans-serif;font-weight:300;color:var(--tan-head);font-size:20px;letter-spacing:.3px;line-height:1}
.h-block{position:absolute;font-family:"Lexend Exa",sans-serif;font-weight:300;color:var(--tan-head);font-size:21px;line-height:24px}
.h-sub{position:absolute;font-family:"Lexend Exa",sans-serif;font-weight:300;color:var(--ink-soft);font-size:11.5px;line-height:15px}
.body-copy{position:absolute;font-size:8.2px;line-height:12.5px;color:var(--ink)}
.body-copy p{margin-bottom:9px}
.obj-list{display:flex;gap:10px;list-style:none}
.obj-list ul{list-style:none}
.obj-list li::before{content:"• ";}
.photo{position:absolute;border-radius:3px}
.chip{position:absolute;display:flex;align-items:center;justify-content:center;text-align:center;font-size:7.4px;line-height:10.5px;font-weight:600;color:#fff;background:var(--tan);padding:0 8px}
.chip-grey{position:absolute;display:flex;align-items:center;justify-content:center;text-align:center;font-size:6.6px;line-height:9.8px;color:var(--ink);background:var(--chip-grey);padding:0 6px}
.comp-box{position:absolute;border:1px solid #b9b9b9;border-radius:2px;background:rgba(255,255,255,.85);text-align:center;font-size:7.6px;line-height:11.5px;color:var(--ink);padding-top:14px}
.comp-box b{display:block;font-weight:600}
.ref-cap{position:absolute;font-size:7.4px;line-height:11px;color:var(--ink)}
.ref-cap b{font-weight:600;display:block}
.ref-cap .meta{display:block;margin-top:11px;color:var(--ink-soft)}
.footer-contact{position:absolute;font-size:7.4px;line-height:11px;color:var(--ink-soft)}
.footer-contact .firm{font-family:"Lexend Exa",sans-serif;font-size:9px;color:var(--ink);margin-bottom:5px;display:block;letter-spacing:.4px}
.brand{position:absolute;font-family:"Lexend Exa",sans-serif;font-weight:400;color:var(--ink)}
.brand .name{font-size:25px;line-height:26px;display:block;letter-spacing:1px}
.brand .line{font-size:13px;line-height:16px;display:block;padding-left:2px}
.brand .mark{position:absolute;left:150px;top:10px;width:13px;height:13px;background:var(--ink)}
.cover-title{position:absolute;font-family:"Lexend Exa",sans-serif;font-weight:400;color:var(--tan-head);font-size:17px}
.cover-sub{position:absolute;font-family:"Lexend Exa",sans-serif;font-weight:300;color:#a9a39a;font-size:11px;line-height:13px}
.guides{position:absolute;left:0;top:0;pointer-events:none}
</style>
</head>
<body>

<div class="stage-dark"></div>
<span class="stage-label" style="left:418px;top:116px">Vorderseite</span>
<span class="stage-label" style="left:725px;top:116px">Rückseite</span>
<span class="stage-label" style="left:580px;top:1046px">Innenseiten</span>

<!-- ============ small front cover ============ -->
<div class="single mini" style="left:268px;top:143px">
  <section class="page page-cover" style="left:0">
    <svg class="bg" viewBox="0 0 480 679"><polygon fill="var(--paper-shade)" points="0,0 480,0 480,170 0,520"/><path fill="var(--cover-dark)" d="M480,167 L118,428 Q100,442 100,470 L100,679 L480,679 Z"/></svg>
    <div class="brand" style="left:153px;top:140px"><span class="name">kernbau</span><span class="line">ingenieure</span><span class="mark"></span></div>
    <div class="cover-title" style="left:140px;top:576px">Kurzportrait</div>
    <div class="cover-sub" style="left:140px;top:606px">Mit uns findet Ihre Vision<br>zur notwendigen Stabilität</div>
  </section>
</div>

<!-- ============ small back page ============ -->
<div class="single mini" style="left:592px;top:143px">
  <section class="page page-back" style="left:0">
    <svg class="bg" viewBox="0 0 480 679"><polygon fill="var(--paper-shade)" points="0,0 400,0 360,230 280,679 0,679"/></svg>
    <h2 class="h-page" style="left:46px;top:87px">Referenzen</h2>
    <div class="photo" role="img" aria-label="Foto des Umbaus Schloss Erlenhof" style="left:46px;top:130px;width:120px;height:85px;background:linear-gradient(160deg,#8eaed0,#b7a58a 55%,#5e6b45)"></div>
    <div class="photo" role="img" aria-label="Luftaufnahme Mehrfamilienhaus im Rohbau" style="left:180px;top:130px;width:120px;height:85px;background:linear-gradient(160deg,#7c8a6a,#9e8577 50%,#6f7f88)"></div>
    <div class="photo" role="img" aria-label="Luftaufnahme Mehrfamilienhäuser Rietheim" style="left:314px;top:130px;width:120px;height:85px;background:linear-gradient(160deg,#8ca06a,#b98d73 50%,#7c9454)"></div>
    <div class="ref-cap" style="left:46px;top:247px;width:130px"><b>Um- &amp; Anbau Schloss Erlenhof<br>Lindwil</b><span class="meta">Bauherr: privat<br>Bauzeit: 2020/21</span></div>
    <div class="ref-cap" style="left:180px;top:247px;width:130px"><b>Mehrfamilienhaus<br>Föhrenstrasse 1, Rietheim</b><span class="meta">Bauherr: Morel Immobilien<br>Bauzeit: 2019/20</span></div>
    <div class="ref-cap" style="left:314px;top:247px;width:160px"><b>Mehrfamilienhaus<br>Rietheim</b><span class="meta">Bauherr: Baugesellschaft Weitblick<br>Bauzeit: 2019/20</span></div>
    <div class="h-sub" style="left:46px;top:353px">Wir sind in der gesammten<br>Deutschschweitz tätig und bieten:</div>
    <div class="chip-grey" style="left:46px;top:395px;width:120px;height:38px">Ein engagiertes &amp; dynamisches Team für tag tägliche Höchstleistungen</div>
    <div class="chip-grey" style="left:46px;top:443px;width:120px;height:40px">Ein fundiertes Fachwissen und innovative Lösungen</div>
    <div class="chip-grey" style="left:46px;top:491px;width:120px;height:42px">Schlanke, optimal auf Ihre Bedürfnisse ausgerichtete Prozesse</div>
    <div class="chip-grey" style="left:180px;top:395px;width:120px;height:32px">Projektbearbeitung nach Wunsch in Deutsch und Englisch</div>
    <div class="chip-grey" style="left:180px;top:443px;width:120px;height:40px">Tägliche Einblicke in alle Facetten des Hochbaus schärfen und den Blickwinkel für Wesentliches</div>
    <div class="chip-grey" style="left:180px;top:491px;width:120px;height:32px">Preiswerte Dienstleistungen bei höchster Arbeitsqualität</div>
    <div class="chip-grey" style="left:314px;top:405px;width:120px;height:38px">Praxisnahes Planen auf dem neuesten Stand der Technik in jeder Ingenieurdisziplin</div>
    <div class="chip-grey" style="left:314px;top:459px;width:120px;height:28px">Partnerschaftlicher Umgang mit allen Projektbeteiligten</div>
    <div class="chip-grey" style="left:314px;top:499px;width:120px;height:28px">Laufende Aus- &amp; Weiterbildung aller Mitarbeiter/innen</div>
    <div class="footer-contact" style="left:46px;top:589px"><span class="firm">kernbau ingenieure gmbh</span>Talackerweg 14 | 8999 Rheinfeld<br>Tel. (+41) 00 310 20 40 | Mobile (+41) 00 310 20 41<br>info@kernbau-ing.example | www.kernbau-ing.example</div>
  </section>
</div>

<!-- ============ small inner spread ============ -->
<div class="spread mini" style="left:280px;top:595px">
  <section class="page page-who" style="left:0">
    <svg class="bg" viewBox="0 0 480 679"><polygon fill="var(--paper-shade)" points="0,0 300,0 480,280 480,600 0,200"/></svg>
    <h2 class="h-page" style="left:46px;top:56px">Wer wir sind</h2>
    <div class="body-copy" style="left:46px;top:98px;width:262px">
      <p>Die kernbau ingenieure GmbH ist ein unabhängiges, junges und dynamisches Bauingenieurbüro aus Rheinfeld. Wir bieten sämtliche Bauingenieurleistungen im Hoch- und konstruktiven Ingenieurbau an.</p>
      <p>Wir planen und realisieren Neu- und Umbauten und führen bei älteren Gebäuden Tragwerkserhaltungen und Verstärkungen durch, womit die Nutzungsdauer erhöht oder eine Umnutzung ermöglicht wird.</p>
      <p>Zu unseren gängigsten Bauobjekten gehören:</p>
      <div class="obj-list"><ul style="width:112px"><li>Wohnungsbauten</li><li>Gewerbe- und Industriebauten</li><li>Öffentliche Bauten</li><li>Pflegeheime</li></ul><ul><li>Landwirtschaftliche Bauten</li><li>Stützbauwerke, Durchlässe,<br>&nbsp;&nbsp;Unterführungen</li><li>Balkonanbauten</li></ul></div>
    </div>
    <div class="photo" role="img" aria-label="Porträtfoto eines Ingenieurs auf einer Baustellenleiter" style="left:314px;top:46px;width:121px;height:168px;background:linear-gradient(170deg,#d8d6d0,#9a948a 45%,#4b5566 70%,#c6bfb2)"></div>
    <h2 class="h-block" style="left:46px;top:300px">Bausteine<br>auf welchen<br>wir aufbauen</h2>
    <div class="chip" style="left:46px;top:408px;width:120px;height:35px">Wir reagieren flexibel auf Bauherrenwünsche</div>
    <div class="chip" style="left:180px;top:408px;width:254px;height:35px">Wir planen Ihr Tragwerk ressourcenschonend mit den minimal notwendigen Abmessungen und Bewehrung</div>
    <div class="chip" style="left:46px;top:455px;width:166px;height:35px">Wir erstellen Pläne mit Top-Zeichnern für die Planung und Ausführung</div>
    <div class="chip" style="left:226px;top:455px;width:208px;height:35px">Wir arbeiten aktiv am Projekt mit und beteiligen uns frühzeitig an der Problemerkennung und Lösung</div>
    <div class="chip" style="left:46px;top:503px;width:208px;height:35px">Wir investieren ins Vorprojekt, damit Probleme frühzeitig vor der Ausführung gelöst werden.</div>
    <div class="chip" style="left:268px;top:503px;width:166px;height:35px">Wir setzen auf ökologische Bauweise, für uns ist Recyclingbeton kein Fremdwort</div>
    <div class="chip" style="left:46px;top:550px;width:120px;height:35px">Breit abgestütztes, harmonierendes Team</div>
    <div class="chip" style="left:180px;top:550px;width:254px;height:35px">Berufsstolz, wir rechnen jedes Tragwerk von Anfang an durch und bestimmen die minimalen Bauteilabmessungen</div>
    <div class="chip" style="left:46px;top:598px;width:120px;height:35px">Wir machen Statik übersichtlich, nachvollziehbar und klar verständlich</div>
    <div class="chip" style="left:180px;top:598px;width:254px;height:35px">Wir erstellen unsere Dokumente im Baukastenprinzip, die Darstellung ist sauber und verständlich</div>
  </section>
  <section class="page page-skills" style="left:480px">
    <svg class="bg" viewBox="0 0 480 679"><polygon fill="var(--paper-shade)" points="0,0 50,0 50,679 0,679"/><polygon fill="var(--paper-warm)" points="330,0 480,0 480,679 60,679 60,560"/><polygon fill="#fff" points="50,0 330,0 60,560 50,679"/></svg>
    <h2 class="h-page" style="left:46px;top:46px">Kompetenzen</h2>
    <div class="h-sub" style="left:46px;top:84px">Klassischer Ingenieurbau<br>Unser Beitrag an Ihrem Bauwerk</div>
    <div class="comp-box" style="left:46px;top:142px;width:188px;height:78px"><b>Tragwerksplanung</b>Tragwerkserhaltung | Tragwerksverstärkung<br>Zustandsuntersuchungen | Statische Nachweise<br>Erdbebensicherheit | Verstärkungskonzepte</div>
    <div class="comp-box" style="left:248px;top:142px;width:187px;height:78px"><b>Baugrube | Baugrubenüberwachung</b>Aushub | Baugrubensicherung | Wasserhaltung<br>Überwachungskonzepte Baugrube &amp;<br>Nachbarparzellen</div>
    <div class="comp-box" style="left:46px;top:234px;width:188px;height:78px"><b>Baupläne</b>Schalungs- &amp; Bewehrungspläne<br>Stahlbau- &amp; Holzbaupläne<br>Aushubpläne inkl. Baugrubensicherungen</div>
    <div class="comp-box" style="left:248px;top:234px;width:187px;height:78px"><b>Digitalisierung</b>Tragwerksmodell inkl. allen statischen Einbauteilen<br>Mengenbestimmung ab Modell<br>Kollisionsprüfung &amp; Qualitätssicherung am Modell</div>
    <div class="comp-box" style="left:46px;top:326px;width:389px;height:78px"><b>Leistungskatalog</b>Abbruch | Unter- &amp; Abfangungen | Schneiden &amp; Bohren<br>Sichern &amp; Ertüchtigen | Kanalisationen | Wasserhaltung | Baugrubenabschlüsse<br>Pfahlfundationen | Aushub | Beton-, Stahl- &amp; Holzbau | Mauerwerk</div>
    <div class="comp-box" style="left:46px;top:419px;width:188px;height:76px"><b>Drohnenflüge</b>Referenzfotos | Rissprotokolle Fassaden &amp;<br>Strassen | Vermessung | Werbevideos</div>
    <div class="comp-box" style="left:248px;top:419px;width:187px;height:76px"><b>Berufsausbildung, unser Beitrag an die Zukunft</b>Lernende ZeichnerIn Fachrichtung Ingenieurbau<br>EFZ Ausbildung Lernende</div>
    <svg class="abs" style="left:0;top:0" width="480" height="679" viewBox="0 0 480 679" fill="#fff" stroke="#8a8a8a" stroke-width="1"><rect x="218" y="134" width="14" height="12"/><rect x="420" y="134" width="14" height="12"/><rect x="218" y="226" width="14" height="12"/><path d="M420,238 l7,-10 l7,10 z"/><rect x="420" y="318" width="14" height="12"/><circle cx="225" cy="418" r="6"/><rect x="420" y="411" width="14" height="12"/></svg>
    <div class="photo" role="img" aria-label="Foto eines modernen weissen Mehrfamilienhauses" style="left:46px;top:521px;width:121px;height:113px;background:linear-gradient(170deg,#b7cde6,#eef0f0 50%,#8f9a7c)"></div>
    <div class="photo" role="img" aria-label="Foto eines dunklen Wohnhauses mit Sichtbeton" style="left:180px;top:521px;width:120px;height:113px;background:linear-gradient(170deg,#c4d3e3,#3e3f42 45%,#a9a7a0)"></div>
    <div class="photo" role="img" aria-label="Luftaufnahme eines Bauernhauses am Hang" style="left:314px;top:521px;width:121px;height:113px;background:linear-gradient(160deg,#7b9456,#a35f45 50%,#5f7a3f)"></div>
  </section>
</div>

<!-- ============ large inner spread with guides ============ -->
<div class="spread" style="left:120px;top:1308px">
  <section class="page page-who" style="left:0">
    <svg class="bg" viewBox="0 0 480 679"><polygon fill="var(--paper-shade)" points="0,0 300,0 480,280 480,600 0,200"/></svg>
    <h2 class="h-page" style="left:46px;top:56px">Wer wir sind</h2>
    <div class="body-copy" style="left:46px;top:98px;width:262px">
      <p>Die kernbau ingenieure GmbH ist ein unabhängiges, junges und dynamisches Bauingenieurbüro aus Rheinfeld. Wir bieten sämtliche Bauingenieurleistungen im Hoch- und konstruktiven Ingenieurbau an.</p>
      <p>Wir planen und realisieren Neu- und Umbauten und führen bei älteren Gebäuden Tragwerkserhaltungen und Verstärkungen durch, womit die Nutzungsdauer erhöht oder eine Umnutzung ermöglicht wird.</p>
      <p>Zu unseren gängigsten Bauobjekten gehören:</p>
      <div class="obj-list"><ul style="width:112px"><li>Wohnungsbauten</li><li>Gewerbe- und Industriebauten</li><li>Öffentliche Bauten</li><li>Pflegeheime</li></ul><ul><li>Landwirtschaftliche Bauten</li><li>Stützbauwerke, Durchlässe,<br>&nbsp;&nbsp;Unterführungen</li><li>Balkonanbauten</li></ul></div>
    </div>
    <div class="photo" role="img" aria-label="Porträtfoto eines Ingenieurs auf einer Baustellenleiter" style="left:314px;top:46px;width:121px;height:168px;background:linear-gradient(170deg,#d8d6d0,#9a948a 45%,#4b5566 70%,#c6bfb2)"></div>
    <h2 class="h-block" style="left:46px;top:300px">Bausteine<br>auf welchen<br>wir aufbauen</h2>
    <div class="chip" style="left:46px;top:408px;width:120px;height:35px">Wir reagieren flexibel auf Bauherrenwünsche</div>
    <div class="chip" style="left:180px;top:408px;width:254px;height:35px">Wir planen Ihr Tragwerk ressourcenschonend mit den minimal notwendigen Abmessungen und Bewehrung</div>
    <div class="chip" style="left:46px;top:455px;width:166px;height:35px">Wir erstellen Pläne mit Top-Zeichnern für die Planung und Ausführung</div>
    <div class="chip" style="left:226px;top:455px;width:208px;height:35px">Wir arbeiten aktiv am Projekt mit und beteiligen uns frühzeitig an der Problemerkennung und Lösung</div>
    <div class="chip" style="left:46px;top:503px;width:208px;height:35px">Wir investieren ins Vorprojekt, damit Probleme frühzeitig vor der Ausführung gelöst werden.</div>
    <div class="chip" style="left:268px;top:503px;width:166px;height:35px">Wir setzen auf ökologische Bauweise, für uns ist Recyclingbeton kein Fremdwort</div>
    <div class="chip" style="left:46px;top:550px;width:120px;height:35px">Breit abgestütztes, harmonierendes Team</div>
    <div class="chip" style="left:180px;top:550px;width:254px;height:35px">Berufsstolz, wir rechnen jedes Tragwerk von Anfang an durch und bestimmen die minimalen Bauteilabmessungen</div>
    <div class="chip" style="left:46px;top:598px;width:120px;height:35px">Wir machen Statik übersichtlich, nachvollziehbar und klar verständlich</div>
    <div class="chip" style="left:180px;top:598px;width:254px;height:35px">Wir erstellen unsere Dokumente im Baukastenprinzip, die Darstellung ist sauber und verständlich</div>
  </section>
  <section class="page page-skills" style="left:480px">
    <svg class="bg" viewBox="0 0 480 679"><polygon fill="var(--paper-shade)" points="0,0 50,0 50,679 0,679"/><polygon fill="var(--paper-warm)" points="330,0 480,0 480,679 60,679 60,560"/><polygon fill="#fff" points="50,0 330,0 60,560 50,679"/></svg>
    <h2 class="h-page" style="left:46px;top:46px">Kompetenzen</h2>
    <div class="h-sub" style="left:46px;top:84px">Klassischer Ingenieurbau<br>Unser Beitrag an Ihrem Bauwerk</div>
    <div class="comp-box" style="left:46px;top:142px;width:188px;height:78px"><b>Tragwerksplanung</b>Tragwerkserhaltung | Tragwerksverstärkung<br>Zustandsuntersuchungen | Statische Nachweise<br>Erdbebensicherheit | Verstärkungskonzepte</div>
    <div class="comp-box" style="left:248px;top:142px;width:187px;height:78px"><b>Baugrube | Baugrubenüberwachung</b>Aushub | Baugrubensicherung | Wasserhaltung<br>Überwachungskonzepte Baugrube &amp;<br>Nachbarparzellen</div>
    <div class="comp-box" style="left:46px;top:234px;width:188px;height:78px"><b>Baupläne</b>Schalungs- &amp; Bewehrungspläne<br>Stahlbau- &amp; Holzbaupläne<br>Aushubpläne inkl. Baugrubensicherungen</div>
    <div class="comp-box" style="left:248px;top:234px;width:187px;height:78px"><b>Digitalisierung</b>Tragwerksmodell inkl. allen statischen Einbauteilen<br>Mengenbestimmung ab Modell<br>Kollisionsprüfung &amp; Qualitätssicherung am Modell</div>
    <div class="comp-box" style="left:46px;top:326px;width:389px;height:78px"><b>Leistungskatalog</b>Abbruch | Unter- &amp; Abfangungen | Schneiden &amp; Bohren<br>Sichern &amp; Ertüchtigen | Kanalisationen | Wasserhaltung | Baugrubenabschlüsse<br>Pfahlfundationen | Aushub | Beton-, Stahl- &amp; Holzbau | Mauerwerk</div>
    <div class="comp-box" style="left:46px;top:419px;width:188px;height:76px"><b>Drohnenflüge</b>Referenzfotos | Rissprotokolle Fassaden &amp;<br>Strassen | Vermessung | Werbevideos</div>
    <div class="comp-box" style="left:248px;top:419px;width:187px;height:76px"><b>Berufsausbildung, unser Beitrag an die Zukunft</b>Lernende ZeichnerIn Fachrichtung Ingenieurbau<br>EFZ Ausbildung Lernende</div>
    <svg class="abs" style="left:0;top:0" width="480" height="679" viewBox="0 0 480 679" fill="#fff" stroke="#8a8a8a" stroke-width="1"><rect x="218" y="134" width="14" height="12"/><rect x="420" y="134" width="14" height="12"/><rect x="218" y="226" width="14" height="12"/><path d="M420,238 l7,-10 l7,10 z"/><rect x="420" y="318" width="14" height="12"/><circle cx="225" cy="418" r="6"/><rect x="420" y="411" width="14" height="12"/></svg>
    <div class="photo" role="img" aria-label="Foto eines modernen weissen Mehrfamilienhauses" style="left:46px;top:521px;width:121px;height:113px;background:linear-gradient(170deg,#b7cde6,#eef0f0 50%,#8f9a7c)"></div>
    <div class="photo" role="img" aria-label="Foto eines dunklen Wohnhauses mit Sichtbeton" style="left:180px;top:521px;width:120px;height:113px;background:linear-gradient(170deg,#c4d3e3,#3e3f42 45%,#a9a7a0)"></div>
    <div class="photo" role="img" aria-label="Luftaufnahme eines Bauernhauses am Hang" style="left:314px;top:521px;width:121px;height:113px;background:linear-gradient(160deg,#7b9456,#a35f45 50%,#5f7a3f)"></div>
  </section>
  <svg class="guides" width="960" height="679" viewBox="0 0 960 679" stroke="var(--guide)" stroke-width="1">
    <path d="M46.5,0V679M166.5,0V679M180.5,0V679M300.5,0V679M314.5,0V679M435.5,0V679M526.5,0V679M646.5,0V679M660.5,0V679M714.5,0V679M728.5,0V679M780.5,0V679M794.5,0V679M915.5,0V679M0,46.5H960M0,636.5H960"/>
  </svg>
</div>

<!-- ============ large back + front with guides ============ -->
<div class="spread" style="left:120px;top:2073px">
  <section class="page page-back" style="left:0">
    <svg class="bg" viewBox="0 0 480 679"><polygon fill="var(--paper-shade)" points="0,0 400,0 360,230 280,679 0,679"/></svg>
    <h2 class="h-page" style="left:46px;top:87px">Referenzen</h2>
    <div class="photo" role="img" aria-label="Foto des Umbaus Schloss Erlenhof" style="left:46px;top:130px;width:120px;height:85px;background:linear-gradient(160deg,#8eaed0,#b7a58a 55%,#5e6b45)"></div>
    <div class="photo" role="img" aria-label="Luftaufnahme Mehrfamilienhaus im Rohbau" style="left:180px;top:130px;width:120px;height:85px;background:linear-gradient(160deg,#7c8a6a,#9e8577 50%,#6f7f88)"></div>
    <div class="photo" role="img" aria-label="Luftaufnahme Mehrfamilienhäuser Rietheim" style="left:314px;top:130px;width:120px;height:85px;background:linear-gradient(160deg,#8ca06a,#b98d73 50%,#7c9454)"></div>
    <div class="ref-cap" style="left:46px;top:247px;width:130px"><b>Um- &amp; Anbau Schloss Erlenhof<br>Lindwil</b><span class="meta">Bauherr: privat<br>Bauzeit: 2020/21</span></div>
    <div class="ref-cap" style="left:180px;top:247px;width:130px"><b>Mehrfamilienhaus<br>Föhrenstrasse 1, Rietheim</b><span class="meta">Bauherr: Morel Immobilien<br>Bauzeit: 2019/20</span></div>
    <div class="ref-cap" style="left:314px;top:247px;width:160px"><b>Mehrfamilienhaus<br>Rietheim</b><span class="meta">Bauherr: Baugesellschaft Weitblick<br>Bauzeit: 2019/20</span></div>
    <div class="h-sub" style="left:46px;top:353px">Wir sind in der gesammten<br>Deutschschweitz tätig und bieten:</div>
    <div class="chip-grey" style="left:46px;top:395px;width:120px;height:38px">Ein engagiertes &amp; dynamisches Team für tag tägliche Höchstleistungen</div>
    <div class="chip-grey" style="left:46px;top:443px;width:120px;height:40px">Ein fundiertes Fachwissen und innovative Lösungen</div>
    <div class="chip-grey" style="left:46px;top:491px;width:120px;height:42px">Schlanke, optimal auf Ihre Bedürfnisse ausgerichtete Prozesse</div>
    <div class="chip-grey" style="left:180px;top:395px;width:120px;height:32px">Projektbearbeitung nach Wunsch in Deutsch und Englisch</div>
    <div class="chip-grey" style="left:180px;top:443px;width:120px;height:40px">Tägliche Einblicke in alle Facetten des Hochbaus schärfen und den Blickwinkel für Wesentliches</div>
    <div class="chip-grey" style="left:180px;top:491px;width:120px;height:32px">Preiswerte Dienstleistungen bei höchster Arbeitsqualität</div>
    <div class="chip-grey" style="left:314px;top:405px;width:120px;height:38px">Praxisnahes Planen auf dem neuesten Stand der Technik in jeder Ingenieurdisziplin</div>
    <div class="chip-grey" style="left:314px;top:459px;width:120px;height:28px">Partnerschaftlicher Umgang mit allen Projektbeteiligten</div>
    <div class="chip-grey" style="left:314px;top:499px;width:120px;height:28px">Laufende Aus- &amp; Weiterbildung aller Mitarbeiter/innen</div>
    <div class="footer-contact" style="left:46px;top:589px"><span class="firm">kernbau ingenieure gmbh</span>Talackerweg 14 | 8999 Rheinfeld<br>Tel. (+41) 00 310 20 40 | Mobile (+41) 00 310 20 41<br>info@kernbau-ing.example | www.kernbau-ing.example</div>
  </section>
  <section class="page page-cover" style="left:480px">
    <svg class="bg" viewBox="0 0 480 679"><polygon fill="var(--paper-shade)" points="0,0 480,0 480,170 0,520"/><path fill="var(--cover-dark)" d="M480,167 L118,428 Q100,442 100,470 L100,679 L480,679 Z"/></svg>
    <div class="brand" style="left:153px;top:140px"><span class="name">kernbau</span><span class="line">ingenieure</span><span class="mark"></span></div>
    <div class="cover-title" style="left:140px;top:576px">Kurzportrait</div>
    <div class="cover-sub" style="left:140px;top:606px">Mit uns findet Ihre Vision<br>zur notwendigen Stabilität</div>
  </section>
  <svg class="guides" width="960" height="679" viewBox="0 0 960 679" stroke="var(--guide)" stroke-width="1">
    <path d="M46.5,0V679M166.5,0V679M180.5,0V679M300.5,0V679M314.5,0V679M435.5,0V679M480.5,0V679M526.5,0V679M580.5,0V679M646.5,0V679M700.5,0V679M714.5,0V679M914.5,0V679M0,42.5H960M0,636.5H960"/>
  </svg>
</div>

</body>
</html>
```